Business card for our start up Automotive Shop

Clean business card design for our new automotive shop Harborline Motor Works. This card will be the template for all of our staff member including technicians and service advisors.

Harborline Motor Works is an automotive service shop catering to US domestic and asian import vehicles. We are a service and maintenance full service facility. Our aim is to provide the best quality workmanship and the best customer service experience in our industry.

Our target market are young professionals to people with families. We are not targeting a younger audience or the car modification scene. The card should be appealing to women of the 30+ age demographic.

We are a shop of younger professionals instead of an older crowd. The card design should reflect as such.

Target Market(s)

30+ Female demographic and 30+ male.

Industry/Entity Type

Automotive

Contact Information for Business Card

Must be clean and appealing to clients. Large enough and easy to read print.

Font styles to use
Sans Serif

Colors
f78f20
ffffff
b2b2b2
dddddd

Requirements
Must have
• Address, website and phone number
• 42-17 58th Ct
• Middle Village NY 11502
• (718) 555-0142
• harborlinemotorworks.example
• There must be an area to add a Name and e-mail address for personalization purposes.
Nice to have
• Back of the card should have website.
• I would also like to incorporate yelp, google+, Facebook, and instagram widgets. Will add the exact pages but everything can be @ or / harborlinemotorworks
• That can be added on the back of the card.

```html
<!DOCTYPE html>
<html lang="en">
<head>
<meta charset="utf-8">
<title>Harborline Motor Works — Business Card</title>
<link rel="stylesheet" href="https://fonts.googleapis.com/css2?family=Exo+2:wght@600;700&family=Open+Sans:wght@400;600&display=swap">
<style>
  :root {
    --orange: #f78f20;
    --white: #ffffff;
    --grey: #b2b2b2;
    --light: #dddddd;
    --ink: #2b2b2b;
    --stage: #efede8;
  }
  * { box-sizing: border-box; margin: 0; padding: 0; }
  html, body { width: 1200px; height: 929px; overflow: hidden; }
  body {
    background: var(--stage);
    font-family: "Open Sans", Arial, sans-serif;
    color: var(--ink);
    position: relative;
  }
  .card {
    position: absolute;
    left: 300px;
    width: 600px;
    height: 343px;
    background: var(--white);
    box-shadow: 0 2px 10px rgba(0,0,0,0.12);
    overflow: hidden;
  }
  .card--back { top: 92px; }
  .card--front { top: 494px; }
  .card__band {
    position: absolute;
    left: 0; right: 0; bottom: 0;
    height: 16px;
    background: var(--orange);
  }

  /* back */
  .brand-mark {
    position: absolute;
    left: 0; right: 0; top: 112px;
    display: flex; align-items: center; justify-content: center; gap: 14px;
  }
  .brand-mark__dot {
    width: 34px; height: 34px; border-radius: 50%;
    background: var(--orange);
  }
  .brand-mark__name {
    font-family: "Exo 2", Arial, sans-serif;
    font-weight: 600;
    font-size: 34px;
    color: var(--orange);
    letter-spacing: 0.5px;
  }
  .social {
    position: absolute;
    right: 28px; bottom: 36px;
    text-align: right;
  }
  .social__icons { display: flex; gap: 5px; justify-content: flex-end; margin-bottom: 4px; }
  .social__icon { width: 11px; height: 11px; border-radius: 50%; background: var(--grey); }
  .social__handle { font-size: 12px; color: var(--ink); }

  /* front */
  .identity {
    position: absolute;
    left: 40px; top: 150px; width: 250px;
    text-align: center;
  }
  .identity__dot {
    width: 58px; height: 58px; border-radius: 50%;
    background: var(--orange);
    margin: 0 auto 14px;
  }
  .identity__name {
    font-family: "Exo 2", Arial, sans-serif;
    font-weight: 600;
    font-size: 24px;
    line-height: 1.15;
    color: var(--orange);
  }
  .divider {
    position: absolute;
    left: 305px; top: 118px;
    width: 1.5px; height: 150px;
    background: var(--orange);
  }
  .contact {
    position: absolute;
    left: 326px; top: 114px;
  }
  .contact__person {
    font-family: "Exo 2", Arial, sans-serif;
    font-weight: 700;
    font-size: 22px;
    color: var(--orange);
    text-transform: uppercase;
    line-height: 1.1;
  }
  .contact__role { font-size: 16px; margin-bottom: 14px; }
  .contact__list { list-style: none; font-size: 13.5px; line-height: 1.45; }
  .contact__list li { display: flex; align-items: flex-start; gap: 7px; }
  .contact__list svg { flex: none; margin-top: 4px; }
  .contact__address { padding-left: 19px; }
</style>
</head>
<body>

<section class="card card--back" aria-label="Business card back">
  <div class="brand-mark">
    <span class="brand-mark__dot"></span>
    <span class="brand-mark__name">Harborline Motor Works</span>
  </div>
  <div class="social">
    <div class="social__icons">
      <span class="social__icon"></span>
      <span class="social__icon"></span>
      <span class="social__icon"></span>
    </div>
    <div class="social__handle">harborlinemotorworks</div>
  </div>
  <div class="card__band"></div>
</section>

<section class="card card--front" aria-label="Business card front">
  <div class="identity">
    <div class="identity__dot"></div>
    <div class="identity__name">Harborline<br>Motor Works</div>
  </div>
  <div class="divider"></div>
  <div class="contact">
    <div class="contact__person">Dana Whitfield</div>
    <div class="contact__role">Founder</div>
    <ul class="contact__list">
      <li>
        <svg width="12" height="14" viewBox="0 0 12 14" aria-hidden="true"><rect x="2.5" y="0.75" width="7" height="12.5" rx="1.3" fill="none" stroke="#f78f20" stroke-width="1.3"/><line x1="5" y1="11" x2="7" y2="11" stroke="#f78f20" stroke-width="1.2"/></svg>
        <span>(718) 555-0142</span>
      </li>
      <li>
        <svg width="12" height="14" viewBox="0 0 12 14" aria-hidden="true"><circle cx="5" cy="5.5" r="3.5" fill="none" stroke="#f78f20" stroke-width="1.6"/><line x1="7.6" y1="8.2" x2="11" y2="11.6" stroke="#f78f20" stroke-width="1.8" stroke-linecap="round"/></svg>
        <span>harborlinemotorworks.example</span>
      </li>
      <li class="contact__address">42-17 58th Ct Middle<br>Village NY 11502</li>
    </ul>
  </div>
  <div class="card__band"></div>
</section>

</body>
</html>
```